Business Card Design

A logo and business card design is required for a new podiatry business based on the Great Ocean Road, Victoria, Australia. The business will provide broad array of podiatry services to communities along the coast.

A distinctive design is sought that represents both professional allied health service delivery and the iconic location of the service, where the ocean meets the Otway ranges. Colours representative of the ocean blues, greens of the local forrest would be desirable.

Target Market(s)

GP's, other allied health professionals, members of the community with foot complaints

Industry/Entity Type

Health

Contact Information for Business Card

Tidewater Bend Podiatry
Gareth Linwell
B.Pod B App Sci (HM)
Phone: 0400 718 306
Email: tidewaterbendpodiatry@mailbrook.net

Requirements
Must have
• On the back of the card room allocated for appointment times.
Nice to have
• Would like the logo to incorporate a foot and the elements of the coast, whether it be ocean &/or the unique elements of the coast and the great ocean road.

```html
<!DOCTYPE html>
<html lang="en">
<head>
<meta charset="utf-8">
<title>Tidewater Bend Podiatry – Business Card</title>
<link rel="stylesheet" href="https://fonts.googleapis.com/css2?family=Open+Sans:ital,wght@0,400;0,600;0,700;1,400&display=swap">
<style>
  :root {
    --canvas-bg: #d9d6d2;
    --card-bg: #f7f5f3;
    --brand-green: #4f9a4c;
    --ocean-blue: #2f7fb9;
    --ink: #141414;
    --ink-soft: #4a4a4a;
    --label-grey: #8a8a8a;
    --rule-grey: #b9b9b9;
    --card-shadow: 0 18px 30px rgba(60, 50, 40, 0.22);
  }
  * { box-sizing: border-box; margin: 0; padding: 0; }
  html, body {
    width: 1200px; height: 800px; overflow: hidden;
    background: var(--canvas-bg);
    font-family: "Open Sans", Arial, sans-serif;
  }
  .canvas { position: relative; width: 1200px; height: 800px; }

  .brand-lockup {
    position: absolute; top: 30px; right: 40px;
    display: flex; align-items: center; gap: 14px;
  }
  .brand-name {
    color: var(--brand-green); font-weight: 600;
    font-size: 32px; line-height: 1.0; text-align: right;
  }
  .brand-square { width: 110px; height: 110px; background: var(--ocean-blue); }

  .card {
    position: absolute; top: 240px;
    width: 520px; height: 318px;
    background: var(--card-bg);
    box-shadow: var(--card-shadow);
  }
  .card--front { left: 60px; }
  .card--back { left: 620px; }

  /* front */
  .card-logo {
    position: absolute; top: 34px; right: 70px;
    display: flex; align-items: center; gap: 12px;
  }
  .card-logo .brand-name { font-size: 27px; }
  .card-logo .brand-square { width: 92px; height: 92px; }

  .holder { position: absolute; left: 44px; top: 160px; }
  .holder-name { font-size: 26px; font-weight: 700; color: var(--ink); }
  .holder-credentials { font-size: 15px; font-style: italic; color: var(--ink-soft); margin-top: 2px; }

  .contact-list { position: absolute; left: 44px; bottom: 34px; list-style: none; }
  .contact-item {
    display: flex; align-items: center; gap: 9px;
    font-size: 15px; color: var(--ink-soft); margin-top: 8px;
  }
  .contact-icon { width: 16px; height: 16px; flex: none; }

  /* back */
  .appointment-title {
    position: absolute; top: 40px; left: 0; right: 0; text-align: center;
    font-size: 18px; font-weight: 700; letter-spacing: 3px; color: var(--ink-soft);
  }
  .appointment-rows { position: absolute; left: 40px; right: 40px; top: 100px; list-style: none; }
  .appointment-row { display: flex; align-items: flex-end; gap: 10px; height: 62px; }
  .field-label {
    font-size: 13px; font-weight: 600; letter-spacing: 1.5px; color: var(--label-grey);
  }
  .field-line { flex: 1; border-bottom: 1px solid var(--rule-grey); height: 1px; margin-bottom: 4px; }
  .field-line--date { flex: 1.4; }
  .field-gap { width: 18px; }
</style>
</head>
<body>
<main class="canvas">

  <div class="brand-lockup">
    <div class="brand-name">Tidewater<br>Bend<br>Podiatry</div>
    <div class="brand-square" aria-hidden="true"></div>
  </div>

  <section class="card card--front" aria-label="Card front">
    <div class="card-logo">
      <div class="brand-name">Tidewater<br>Bend<br>Podiatry</div>
      <div class="brand-square" aria-hidden="true"></div>
    </div>

    <div class="holder">
      <h1 class="holder-name">Gareth Linwell</h1>
      <p class="holder-credentials">B.Pod B App Sci (HM)</p>
    </div>

    <ul class="contact-list">
      <li class="contact-item">
        <svg class="contact-icon" viewBox="0 0 16 16" aria-hidden="true">
          <path d="M4 1.5 L6 4.5 L4.6 6 C5.5 8 7.8 10.4 10 11.4 L11.5 10 L14.5 12 L13 14.5 C8 14.5 1.5 8 1.5 3 Z" fill="none" stroke="var(--brand-green)" stroke-width="1.5" stroke-linejoin="round"/>
        </svg>
        0400 718 306
      </li>
      <li class="contact-item">
        <svg class="contact-icon" viewBox="0 0 16 16" aria-hidden="true">
          <rect x="1.5" y="3.5" width="13" height="9" fill="none" stroke="var(--brand-green)" stroke-width="1.5"/>
          <path d="M1.5 3.5 L8 9 L14.5 3.5" fill="none" stroke="var(--brand-green)" stroke-width="1.5"/>
        </svg>
        tidewaterbendpodiatry@mailbrook.net
      </li>
    </ul>
  </section>

  <section class="card card--back" aria-label="Card back">
    <h2 class="appointment-title">APPOINTMENT</h2>
    <ul class="appointment-rows">
      <li class="appointment-row">
        <span class="field-label">DATE</span><span class="field-line field-line--date"></span>
        <span class="field-gap"></span>
        <span class="field-label">TIME</span><span class="field-line"></span>
      </li>
      <li class="appointment-row">
        <span class="field-label">DATE</span><span class="field-line field-line--date"></span>
        <span class="field-gap"></span>
        <span class="field-label">TIME</span><span class="field-line"></span>
      </li>
      <li class="appointment-row">
        <span class="field-label">DATE</span><span class="field-line field-line--date"></span>
        <span class="field-gap"></span>
        <span class="field-label">TIME</span><span class="field-line"></span>
      </li>
    </ul>
  </section>

</main>
</body>
</html>
```